Book cover design, title is "Go Solo Now: How to Swap Your Salary in 10 Seasons"

Design a cover for a book about freelancing. Example of my previous book's cover attached. Book title is "Go Solo Now: How to Swap Your Salary in 10 Seasons". Looking to target people who have a 9-5 job but are seeking to try out freelancing as a way to supplement income and eventually quit their day job.

Target Market(s)

Looking to target people who have a 9-5 job but are seeking to try out freelancing as a way to supplement income and eventually quit their day job.

Industry/Entity Type

Consulting

Font styles to use
Serif
Sans Serif

Colors

Designer to choose colors to be used in the design.

Requirements
Must have
• I love these books covers...
• https://www.pagelodge.example/Tame-Notebin-Casual-Sorting-Settled-ebook/dp/Q71MWRTZPA/ref=asap_bc?ie=UTF8
• https://www.pagelodge.example/Bright-Dawn-Scribes-Drafting-Doubles/dp/5830617294/ref=asap_bc?ie=UTF8
• https://www.pagelodge.example/Way-Pen-Factual-eBook-Weeks-ebook/dp/Q93KT41ZXN/ref=asap_bc?ie=UTF8
• https://www.pagelodge.example/Ritual-Piling-Tiny-Shifts-Moments/dp/6027158392/ref=asap_bc?ie=UTF8
• https://www.pagelodge.example/Boost-Each-Hour-Core-ebook/dp/Q82WFN6JTM/ref=asap_bc?ie=UTF8
• https://www.pagelodge.example/Artisan-Co-Total-Thriving-Gig-ebook/dp/Q66813XKVR/ref=sr_1_4?ie=UTF8&qid=2738405519&sr=8-4&keywords=freelancing
Should not have
• Don't submit 3D renderings, just the front cover image please.

```html
<!DOCTYPE html>
<html lang="en">
<head>
<meta charset="utf-8">
<title>Go Solo Now — Book Cover</title>
<link href="https://fonts.googleapis.com/css2?family=Roboto:wght@300;700&family=Roboto+Condensed:wght@500&family=Josefin+Sans:wght@400&display=swap" rel="stylesheet">
<style>
  :root {
    --night-teal: #1d5068;
    --deep-navy: #0f2a3b;
    --ink-blue: #173f55;
    --title-white: #ffffff;
    --accent-orange: #f19a3a;
    --lamp-amber: #f2b765;
    --warm-ochre: #e3913f;
    --burnt-orange: #cf7a30;
    --author-ink: #1c1c1c;
  }
  * { margin: 0; padding: 0; box-sizing: border-box; }
  html, body {
    width: 788px;
    height: 1200px;
    overflow: hidden;
    background: var(--deep-navy);
  }
  .cover {
    position: relative;
    width: 788px;
    height: 1200px;
    overflow: hidden;
    background:
      radial-gradient(ellipse at 88% 8%, rgba(80, 150, 170, 0.35), transparent 50%),
      radial-gradient(ellipse at 10% 45%, rgba(40, 100, 120, 0.25), transparent 55%),
      linear-gradient(180deg, var(--night-teal) 0%, var(--ink-blue) 55%, var(--deep-navy) 100%);
  }
  .title {
    position: absolute;
    top: 100px;
    left: 0;
    width: 100%;
    text-align: center;
    color: var(--title-white);
    font-family: "Roboto", sans-serif;
    text-transform: uppercase;
    line-height: 1;
  }
  .title-lead {
    display: block;
    font-weight: 300;
    font-size: 100px;
    letter-spacing: 2px;
  }
  .title-main {
    display: block;
    margin-top: 20px;
    font-weight: 700;
    font-size: 100px;
    letter-spacing: 3px;
  }
  .subtitle {
    position: absolute;
    top: 378px;
    left: 0;
    width: 100%;
    text-align: center;
    color: var(--accent-orange);
    font-family: "Roboto Condensed", sans-serif;
    font-weight: 500;
    font-size: 37px;
    letter-spacing: 1.5px;
    text-transform: uppercase;
    line-height: 1;
  }
  .subtitle-line { display: block; }
  .subtitle-line + .subtitle-line {
    margin-top: 8px;
    display: flex;
    justify-content: center;
    align-items: center;
    gap: 10px;
  }
  .number-badge {
    display: inline-flex;
    align-items: center;
    justify-content: center;
    width: 48px;
    height: 48px;
    border-radius: 50%;
    background: var(--title-white);
    color: var(--accent-orange);
    font-size: 30px;
  }
  .illustration {
    position: absolute;
    left: 0;
    top: 600px;
    width: 788px;
    height: 600px;
    background:
      radial-gradient(circle at 84% 24%, rgba(242, 183, 101, 0.9) 0, rgba(242, 183, 101, 0.35) 60px, transparent 130px),
      radial-gradient(ellipse 62% 80% at 40% 72%, var(--lamp-amber) 0%, var(--warm-ochre) 45%, rgba(207, 122, 48, 0.75) 68%, rgba(207, 122, 48, 0) 100%),
      linear-gradient(180deg, transparent 0%, rgba(227, 145, 63, 0.35) 100%);
  }
  .author {
    position: absolute;
    bottom: 28px;
    left: 0;
    width: 100%;
    text-align: center;
    color: var(--author-ink);
    font-family: "Josefin Sans", sans-serif;
    font-weight: 400;
    font-size: 44px;
    letter-spacing: 2px;
    text-transform: uppercase;
  }
</style>
</head>
<body>
  <main class="cover">
    <div class="illustration" role="img" aria-label="Warm orange silhouette of a young man working at a typewriter late at night beside a glowing desk lamp"></div>
    <h1 class="title">
      <span class="title-lead">Go Solo</span>
      <span class="title-main">Now</span>
    </h1>
    <p class="subtitle">
      <span class="subtitle-line">How to swap your salary in</span>
      <span class="subtitle-line"><span class="number-badge">10</span> Seasons</span>
    </p>
    <p class="author">Adrien Beaulieu</p>
  </main>
</body>
</html>
```